Real Estate Sign 24" wide X 36" long

We are looking for creative modern design for a real estate sign, Wow us but remember its about people driving by the sign and retaining our brand.

The Brixley Marsh Logo need to be at the bottom of sign. Please use change colors to fit your design.

Also need the following on the sign:

555.318.4062
Ned Calloway Silas Pruett
Calloway & Pruett Logo
Ned and Silas's picture

Our current sign we are replacing is attached: "Thornbury C&P". We are replacing for more modern beautiful design that is one piece.

A rough draft is also attached...but be creative...don't think inside a box.

Target Market(s)

Home Buyers and Sellers

Industry/Entity Type

Real Estate Agent

Colors

Designer to choose colors to be used in the design.

Requirements
Must have
• The sign must be 24" wide X 36" tall. This will be the sign we hang in front of homes for sale.
Nice to have
• Background design that works well would be nice.
• Our business is in Florida...would be nice to have background palm trees, sun, beach...but not necessary.

```html
<!DOCTYPE html>
<html lang="en">
<head>
<meta charset="utf-8">
<title>Calloway &amp; Pruett Realty Group – Yard Sign</title>
<link href="https://fonts.googleapis.com/css2?family=Montserrat:wght@300;400;500&family=Libre+Baskerville:wght@400&display=swap" rel="stylesheet">
<style>
  :root{
    --teal:#2a9aa3;
    --teal-dark:#1d7f89;
    --navy:#1c2a55;
    --navy-deep:#142046;
    --white:#ffffff;
    --backdrop:#eef1f4;
    --slate:#5d6f86;
  }
  *{margin:0;padding:0;box-sizing:border-box}
  html,body{width:1200px;height:1200px;overflow:hidden;background:var(--backdrop)}
  .sign{
    position:absolute;left:240px;top:60px;width:720px;height:1080px;
    background:var(--white);overflow:hidden;
    box-shadow:0 8px 30px rgba(20,32,70,.18);
  }
  .brand{
    position:absolute;top:150px;left:0;width:100%;text-align:center;
    font-family:"Montserrat",sans-serif;color:var(--teal);
  }
  .brand-name{font-weight:400;font-size:58px;letter-spacing:1px;line-height:1}
  .brand-tag{font-weight:400;font-size:17px;letter-spacing:6px;margin-top:10px;color:var(--teal)}
  .phone{
    position:absolute;top:300px;width:100%;text-align:center;
    font-family:"Libre Baskerville",serif;font-size:86px;color:var(--navy);letter-spacing:1px;
  }
  .web{
    position:absolute;top:432px;width:100%;text-align:center;
    font-family:"Montserrat",sans-serif;font-weight:500;font-size:34px;color:var(--teal);
  }
  .band{position:absolute;left:0;top:500px;width:720px;height:580px}
  .agents-photo{
    position:absolute;left:150px;top:700px;width:460px;height:320px;
    background:linear-gradient(180deg,#3b4a72 0%,#2a3760 55%,#1c2a55 100%);
    border-radius:4px;opacity:.9;
  }
  .agent-names{
    position:absolute;top:1032px;left:150px;width:460px;display:flex;justify-content:space-around;
    font-family:"Montserrat",sans-serif;font-size:17px;color:var(--white);
  }
  .brokerage{
    position:absolute;left:26px;top:1034px;
    font-family:"Montserrat",sans-serif;font-weight:500;font-size:14px;letter-spacing:2px;
    color:var(--white);text-transform:uppercase;
  }
</style>
</head>
<body>
  <main class="sign">
    <svg class="band" viewBox="0 0 720 580" width="720" height="580" aria-hidden="true">
      <path d="M0 170 C 200 60, 460 20, 720 40 L720 580 L0 580 Z" fill="var(--teal)"/>
      <path d="M0 205 C 220 95, 470 62, 720 70 L720 580 L0 580 Z" fill="var(--white)"/>
      <path d="M0 235 C 230 125, 480 95, 720 100 L720 580 L0 580 Z" fill="var(--navy)"/>
      <rect x="0" y="330" width="150" height="250" fill="var(--navy-deep)" opacity=".35" role="img" aria-label="Faint palm tree silhouettes"/>
    </svg>

    <header class="brand">
      <div class="brand-name">Calloway &amp; Pruett</div>
      <div class="brand-tag">REALTY GROUP</div>
    </header>
    <div class="phone">555.318.4062</div>
    <div class="web">CallowayPruettRealty.com</div>

    <div class="agents-photo" role="img" aria-label="Portrait photo of agents Ned Calloway and Silas Pruett"></div>
    <div class="agent-names"><span>Ned Calloway</span><span>Silas Pruett</span></div>
    <div class="brokerage">Brixley Marsh</div>
  </main>
</body>
</html>
```